Business Card Design for Marketing Firm

Looking for business card design for higher end marketing firm. Clean but impressionable/trendy. We are a marketing firm that represents manufacturers in the foodservice equipment and supply industry. Our customers are end users such has hotels, restaurants, country clubs, convention centers and casinos as well as distributors of restaurants supplies and equipment, and manufacturers of foodservice equipment and supplies.
Target Market(s)
Hotels, Restaurants, Supply & Equipment Distributors, Foodservice Manufacturers
Industry/Entity Type
Foodservice/Hospitality
Contact Information for Business Card
Name, Title, Contact Number, Email, Website, Social Media, Address
Requirements
Must have
- Clean & Simple but Serious and Impressionable

```html
<!DOCTYPE html>
<html lang="en">
<head>
<meta charset="utf-8">
<title>Meridian Hospitality Reps – Business Card</title>
<link rel="stylesheet" href="https://fonts.googleapis.com/css2?family=Cinzel:wght@400;700&family=Arimo:wght@400;700&display=swap">
<style>
  :root {
    --navy: #03036e;
    --paper: #f4f4f6;
    --ink: #222226;
    --muted: #7a7a80;
    --backdrop: #7f7f7f;
    --white: #ffffff;
  }
  * { box-sizing: border-box; margin: 0; padding: 0; }
  html, body {
    width: 1200px; height: 900px; overflow: hidden;
    background: var(--backdrop);
  }
  .stage {
    position: relative; width: 1200px; height: 900px;
  }
  .card {
    position: absolute; left: 300px; width: 600px; height: 343px;
    border-radius: 26px; overflow: hidden;
  }
  /* Front */
  .card--front { top: 77px; background: var(--navy); color: var(--white); }
  .front-mark {
    position: absolute; left: 50%; top: 54px; transform: translateX(-50%);
  }
  .wordmark {
    position: absolute; left: 50%; top: 146px; transform: translateX(-50%);
    width: 420px; text-align: center;
  }
  .wordmark__name {
    font-family: "Cinzel", serif; font-weight: 400; font-size: 33px;
    letter-spacing: 1px; white-space: nowrap; line-height: 1;
  }
  .wordmark__rule {
    height: 1.5px; background: var(--white); margin-top: 10px;
  }
  .wordmark__sub {
    font-family: "Cinzel", serif; font-weight: 400; font-size: 17px;
    text-align: right; margin-top: 4px; letter-spacing: 1px;
  }
  .front-web {
    position: absolute; left: 0; right: 0; top: 270px; text-align: center;
    font-family: "Arimo", sans-serif; font-size: 14px; letter-spacing: 3px;
  }
  /* Back */
  .card--back { top: 480px; background: var(--paper); color: var(--ink); }
  .back-brand {
    position: absolute; right: 48px; top: 54px;
    font-family: "Cinzel", serif; font-weight: 700; font-size: 30px;
    color: var(--navy); letter-spacing: 1px;
  }
  .social { position: absolute; left: 46px; top: 80px; display: flex; gap: 6px; }
  .social__dot { width: 20px; height: 20px; border-radius: 50%; background: var(--navy); }
  .person { position: absolute; left: 60px; top: 196px; font-family: "Arimo", sans-serif; }
  .person__name {
    font-family: "Cinzel", serif; font-weight: 700; font-size: 25px;
    color: var(--navy); letter-spacing: 0.5px; line-height: 1;
  }
  .person__title { font-size: 15px; color: var(--muted); margin-top: 3px; }
  .contact-line { font-size: 15px; margin-top: 6px; color: var(--ink); }
  .contact-line .label { color: var(--navy); font-weight: 700; margin-right: 4px; }
  .address { font-size: 15px; margin-top: 14px; line-height: 1.3; }
  .divider {
    position: absolute; left: 330px; top: 206px; width: 1px; height: 80px;
    background: var(--navy); opacity: 0.7;
  }
  .online { position: absolute; left: 352px; top: 214px; font-family: "Arimo", sans-serif; }
  .online .contact-line { margin-top: 2px; }
</style>
</head>
<body>
<main class="stage">
  <section class="card card--front">
    <svg class="front-mark" width="60" height="60" viewBox="0 0 60 60" aria-hidden="true">
      <circle cx="30" cy="30" r="27" fill="none" stroke="#ffffff" stroke-width="2"/>
    </svg>
    <div class="wordmark">
      <div class="wordmark__name">Meridian Hospitality</div>
      <div class="wordmark__rule"></div>
      <div class="wordmark__sub">Reps</div>
    </div>
    <div class="front-web">www.MERIDIAN.com</div>
  </section>

  <section class="card card--back">
    <div class="social" aria-label="Social media">
      <span class="social__dot"></span>
      <span class="social__dot"></span>
      <span class="social__dot"></span>
    </div>
    <div class="back-brand">Meridian</div>

    <div class="person">
      <div class="person__name">Marcus Hale</div>
      <div class="person__title">President</div>
      <div class="contact-line"><span class="label">P :</span>(555) 0142-7781</div>
      <div class="address">2716 Harbor View Lane<br>Glen Cove, NY 11542</div>
    </div>

    <div class="divider"></div>

    <div class="online">
      <div class="contact-line"><span class="label">E :</span>name@MERIDIAN.com</div>
      <div class="contact-line"><span class="label">W :</span>www.MERIDIAN.com</div>
    </div>
  </section>
</main>
</body>
</html>
```